New Branding Business Card Design

Redesign business card according to new branding update.

** The design received so far are single color + BLACK.
I'd encourage designer to use different tones of blue / purple as described in the Designer Brief color palette

Target Market(s)

International

Industry/Entity Type

Medical Equipment

Contact Information for Business Card

Logo on one side (Designer can decide if they want to move certain info from the other side to save space)

Main body info (company name, individual name in both English and Chinese, contact info etc) on the other
Prefer a 'cleaner' layout - vs 'all over the place'
Prefer flush left alignment

Font styles to use
Sans Serif

Requirements
Must have
• Key info
• (Company name (English)): VORAM (HK) Limited
• (Name (English)): Marcus L. Pryde
• (Credential): FCPA, FHKSI
• (Title): Founder, Managing Director & CEO
• For the following info, designers decide whether to use colon or no colon, stroke separator, or use icon gfx for T (for telephone fixed line, M for mobile etc.)
• T: +852 3517 VORAM / +852 3517 4062
• M: +852 6243 7719 / + 86 139 2745 3186
• E: marcus.l.pryde@voram-example.hk
Nice to have
• Depending on the space and spacing available designers can add or use fuller title and other info
• Title: Chairman of the Executive Committee, Founder, Managing Director & CEO
• (Name (Chinese)): 林書恒
Should not have
• One of our business entities a long company name that cannot be broken into 2 lines
• makes vertical implementation almost impossible

```html
<!DOCTYPE html>
<html lang="en">
<head>
<meta charset="utf-8">
<title>VORAM Business Card</title>
<link rel="stylesheet" href="https://fonts.googleapis.com/css2?family=Poppins:wght@400;500;600&family=Noto+Sans+TC:wght@500&display=swap">
<style>
  :root {
    --purple: #5a2a8a;
    --ink: #2a2a2a;
    --card: #ffffff;
    --backdrop: #e9e7ec;
  }
  html, body {
    margin: 0;
    padding: 0;
    width: 1200px;
    height: 1040px;
    overflow: hidden;
    background: var(--backdrop);
    font-family: "Poppins", sans-serif;
  }
  .canvas {
    position: relative;
    width: 1200px;
    height: 1040px;
  }
  .card {
    position: absolute;
    left: 250px;
    width: 700px;
    height: 400px;
    background: var(--card);
    border-radius: 28px;
    box-shadow: 0 6px 18px rgba(0,0,0,0.12);
  }
  .card--front { top: 60px; }
  .card--back { top: 560px; }

  .details {
    position: absolute;
    left: 52px;
    bottom: 46px;
    color: var(--ink);
  }
  .name-zh {
    font-family: "Noto Sans TC", sans-serif;
    font-weight: 500;
    font-size: 15px;
    color: var(--purple);
    margin: 0;
    line-height: 1.2;
  }
  .name {
    margin: 0;
    font-size: 31px;
    font-weight: 600;
    color: var(--purple);
    line-height: 1.1;
  }
  .credentials {
    font-size: 15px;
    font-weight: 500;
  }
  .title {
    margin: 4px 0 0;
    font-size: 15px;
    font-weight: 400;
  }
  .company {
    margin: 14px 0 14px;
    font-size: 16px;
    font-weight: 500;
    color: var(--purple);
  }
  .contacts {
    list-style: none;
    margin: 0;
    padding: 0;
    font-size: 14px;
    line-height: 1.55;
  }
  .contacts li {
    display: flex;
    align-items: center;
    gap: 10px;
  }
  .contacts svg {
    width: 14px;
    height: 14px;
    flex: none;
  }

  .brand {
    position: absolute;
    left: 48px;
    bottom: 44px;
    display: flex;
    align-items: center;
    gap: 12px;
  }
  .brand-mark {
    width: 34px;
    height: 34px;
    border-radius: 6px;
    background: var(--purple);
  }
  .brand-name {
    font-size: 30px;
    font-weight: 600;
    color: var(--purple);
    letter-spacing: 1px;
  }
</style>
</head>
<body>
<main class="canvas">
  <section class="card card--front" aria-label="Card front">
    <div class="details">
      <p class="name-zh">林書恒</p>
      <h1 class="name">Marcus L. Pryde <span class="credentials">FCPA, FHKSI</span></h1>
      <p class="title">Founder, Managing Director &amp; CEO</p>
      <p class="company">VORAM (HK) Limited</p>
      <ul class="contacts">
        <li>
          <svg viewBox="0 0 16 16" aria-hidden="true"><path fill="var(--purple)" d="M3.5 1.5l2.5 0 1 3.5-1.8 1.2c.8 1.8 2.1 3.1 3.9 3.9L10.3 8.3l3.5 1v2.5c0 1-.9 1.8-1.9 1.7C6.5 13 2.9 9.5 1.8 3.4 1.7 2.4 2.5 1.5 3.5 1.5z"/></svg>
          +852 3517 VORAM / +852 3517 4062
        </li>
        <li>
          <svg viewBox="0 0 16 16" aria-hidden="true"><rect x="4" y="1.5" width="8" height="13" rx="1.5" fill="none" stroke="var(--purple)" stroke-width="1.6"/><circle cx="8" cy="12" r="0.9" fill="var(--purple)"/></svg>
          +852 6243 7719 / + 86 139 2745 3186
        </li>
        <li>
          <svg viewBox="0 0 16 16" aria-hidden="true"><rect x="1.5" y="3.5" width="13" height="9" rx="1" fill="var(--purple)"/><path d="M2 4l6 5 6-5" fill="none" stroke="#fff" stroke-width="1.2"/></svg>
          marcus.l.pryde@voram-example.hk
        </li>
      </ul>
    </div>
  </section>

  <section class="card card--back" aria-label="Card back">
    <div class="brand">
      <span class="brand-mark" aria-hidden="true"></span>
      <span class="brand-name">VORAM</span>
    </div>
  </section>
</main>
</body>
</html>
```